VelaCure Wellness Business Cards

I am looking to have luxury business cards made for my IV Therapy and Wellness business.
Updates

Target Market(s)

Health and Wellness professionals

Industry/Entity Type

MedSpa

Contact Information for Business Card

Tobin Haverly, MSN, RN, CCRN Tobin@velacurewellness.com (916) 582-3179 QR code to website www.velacurewellness.com

```html
<!DOCTYPE html>
<html lang="en">
<head>
<meta charset="UTF-8">
<title>VelaCure Wellness Business Cards</title>
<link href="https://fonts.googleapis.com/css2?family=Poppins:wght@300;400;600;700&display=swap" rel="stylesheet">
<style>
  :root {
    --navy: #1e1f5e;
    --sky: #1fa8e0;
    --white: #ffffff;
    --backdrop: #e4e4e6;
  }
  * { box-sizing: border-box; margin: 0; padding: 0; }
  html, body { width: 1200px; height: 900px; overflow: hidden; }
  body {
    background: var(--backdrop);
    font-family: "Poppins", sans-serif;
    color: var(--navy);
    position: relative;
  }
  .card {
    position: absolute;
    width: 560px;
    height: 320px;
    border-radius: 26px;
    overflow: hidden;
  }
  .card-front { left: 120px; top: 110px; background: var(--white); }
  .card-back { left: 520px; top: 470px; background: var(--navy); }

  /* front */
  .front-brand {
    position: absolute;
    left: 40px; top: 120px;
    width: 220px;
    font-weight: 700;
    font-size: 30px;
    line-height: 1.05;
    color: var(--navy);
  }
  .front-divider {
    position: absolute;
    left: 282px; top: 70px;
    width: 2px; height: 180px;
    background: var(--navy);
  }
  .holder { position: absolute; left: 312px; top: 74px; width: 230px; }
  .holder-name { font-weight: 700; font-size: 25px; line-height: 1.1; }
  .holder-role { font-weight: 400; font-size: 17px; margin-top: 2px; }
  .holder-rule {
    height: 2px; width: 220px; background: var(--sky);
    margin: 10px 0 16px;
  }
  .contact-list { list-style: none; }
  .contact-item {
    display: flex; align-items: center; gap: 9px;
    font-size: 12px; font-weight: 400;
    margin-bottom: 9px;
  }
  .contact-icon { width: 14px; height: 14px; flex: none; }

  /* back */
  .back-brand {
    position: absolute;
    top: 70px;
    color: var(--white);
    font-weight: 600;
    font-size: 28px;
    line-height: 1.05;
    width: 200px;
  }
  .back-brand-primary { left: 50px; }
  .back-brand-secondary { left: 320px; top: 118px; font-weight: 600; }
  .back-divider {
    position: absolute;
    left: 290px; top: 60px;
    width: 1.5px; height: 150px;
    background: rgba(255,255,255,0.7);
  }
  .url-pill {
    position: absolute;
    left: 40px; bottom: 46px;
    width: 250px; height: 34px;
    border-radius: 17px;
    background: var(--sky);
    color: var(--white);
    font-size: 13px;
    letter-spacing: 2px;
    display: flex; align-items: center; justify-content: center;
  }
</style>
</head>
<body>
  <section class="card card-front">
    <div class="front-brand">VelaCure Wellness</div>
    <div class="front-divider"></div>
    <div class="holder">
      <p class="holder-name">Your Name Here</p>
      <p class="holder-role">Your Designation</p>
      <div class="holder-rule"></div>
      <ul class="contact-list">
        <li class="contact-item">
          <svg class="contact-icon" viewBox="0 0 24 24"><path fill="#1fa8e0" d="M6.6 10.8a15 15 0 0 0 6.6 6.6l2.2-2.2a1 1 0 0 1 1-.25 11.4 11.4 0 0 0 3.6.57 1 1 0 0 1 1 1V20a1 1 0 0 1-1 1A17 17 0 0 1 3 4a1 1 0 0 1 1-1h3.5a1 1 0 0 1 1 1c0 1.25.2 2.45.57 3.57a1 1 0 0 1-.25 1z"/></svg>
          (916) 582-3179
        </li>
        <li class="contact-item">
          <svg class="contact-icon" viewBox="0 0 24 24"><rect x="2" y="5" width="20" height="14" rx="1" fill="#1fa8e0"/><path d="M2 6l10 7 10-7" fill="none" stroke="#fff" stroke-width="1.6"/></svg>
          Tobin@velacurewellness.com
        </li>
        <li class="contact-item">
          <svg class="contact-icon" viewBox="0 0 24 24" fill="none" stroke="#1fa8e0" stroke-width="1.8"><circle cx="12" cy="12" r="9"/><ellipse cx="12" cy="12" rx="4" ry="9"/><path d="M3 12h18M5 7h14M5 17h14"/></svg>
          www.velacurewellness.com
        </li>
      </ul>
    </div>
  </section>

  <section class="card card-back">
    <div class="back-brand back-brand-primary">VelaCure Wellness</div>
    <div class="back-divider"></div>
    <div class="back-brand back-brand-secondary">VelaCure Wellness</div>
    <div class="url-pill">www.velacurewellness.com</div>
  </section>
</body>
</html>
```